IT Company based on Biology Business Needs a PowerPoint Design

We need a powerpoint design for a new company called 'Tall FERN'. We develop the machine learning solutions especially focused on deep learning algorithms for biology industry. Our initial product is a vision detection on biological images to help doctors diagnose the symptoms. We would like to see designs that use the color green.

Industry/Entity Type

Biotechnology

Requirements
Nice to have
• Lots of slide templates with company logo's look and feel

```html
<!DOCTYPE html>
<html lang="en">
<head>
<meta charset="UTF-8">
<title>Tall FERN – Timeline Slide</title>
<link href="https://fonts.googleapis.com/css2?family=Oxygen:wght@400;700&family=Roboto:wght@400;700&family=Signika:wght@600;700&display=swap" rel="stylesheet">
<style>
  :root {
    --green-dark: #128c44;
    --green-light: #7dc242;
    --grey-dark: #5e5e5e;
    --text: #333333;
    --panel-bg: #f3f4f6;
    --rule: #cfcfcf;
    --footer: #d6d6d6;
    --white: #ffffff;
  }
  * { margin: 0; padding: 0; box-sizing: border-box; }
  html, body { width: 1200px; height: 900px; overflow: hidden; background: var(--white); }
  .slide { position: relative; width: 1200px; height: 900px; overflow: hidden; background: var(--white); font-family: "Roboto", Arial, sans-serif; }

  .header { position: absolute; left: 0; top: 0; width: 1200px; height: 87px; background: var(--green-dark); }
  .header-rule { position: absolute; left: 0; top: 90px; width: 1200px; height: 4px; background: var(--green-light); }
  .slide-title { position: absolute; left: 27px; top: 18px; font-family: "Oxygen", Arial, sans-serif; font-weight: 400; font-size: 36px; color: var(--white); letter-spacing: 0.5px; }
  .brand { position: absolute; right: 12px; top: 24px; display: flex; align-items: center; gap: 10px; }
  .brand-dot { width: 22px; height: 22px; border-radius: 50%; background: var(--white); }
  .brand-name { font-family: "Oxygen", Arial, sans-serif; font-weight: 400; font-size: 27px; color: var(--white); }

  .backdrop-art { position: absolute; left: 700px; top: 120px; width: 500px; height: 720px; background: radial-gradient(ellipse at 55% 40%, rgba(235,235,235,0.7), rgba(255,255,255,0) 70%); }

  .lead { position: absolute; left: 55px; top: 126px; font-weight: 700; font-size: 22px; color: var(--green-light); }
  .intro { position: absolute; left: 55px; top: 175px; width: 1040px; font-size: 18px; line-height: 30px; color: var(--text); }

  .timeline-line { position: absolute; left: 225px; top: 355px; width: 755px; height: 3px; background: var(--rule); }
  .milestone { position: absolute; top: 301px; width: 110px; height: 110px; border-radius: 50%; background: var(--white); border: 3px solid #c9c9c9; display: flex; align-items: center; justify-content: center; }
  .milestone span { width: 92px; height: 92px; border-radius: 50%; display: flex; align-items: center; justify-content: center; font-weight: 700; font-size: 27px; color: var(--white); }

  .card { position: absolute; top: 417px; width: 331px; height: 396px; background: var(--panel-bg); border: 2px solid; border-radius: 4px; }
  .card-head { height: 62px; display: flex; align-items: center; justify-content: center; font-family: "Signika", Arial, sans-serif; font-weight: 700; font-size: 23px; color: var(--white); position: relative; }
  .card-head::before { content: ""; position: absolute; top: -14px; left: 50%; margin-left: -14px; border-left: 14px solid transparent; border-right: 14px solid transparent; border-bottom: 14px solid; border-bottom-color: inherit; }
  .card-body { padding: 30px 0 0 35px; width: 290px; font-size: 18px; line-height: 30px; color: var(--text); }

  .is-green { border-color: var(--green-dark); }
  .is-green .card-head, .is-green.milestone-fill { background: var(--green-dark); border-bottom-color: var(--green-dark); }
  .is-lime { border-color: var(--green-light); }
  .is-lime .card-head, .is-lime.milestone-fill { background: var(--green-light); border-bottom-color: var(--green-light); }
  .is-grey { border-color: var(--grey-dark); }
  .is-grey .card-head, .is-grey.milestone-fill { background: var(--grey-dark); border-bottom-color: var(--grey-dark); }

  .footer { position: absolute; left: 0; top: 875px; width: 1200px; height: 25px; background: var(--footer); }
</style>
</head>
<body>
<div class="slide">
  <div class="backdrop-art" role="img" aria-label="Faint molecule-style decoration"></div>

  <div class="header">
    <h1 class="slide-title">Project Title Here</h1>
    <div class="brand"><span class="brand-dot"></span><span class="brand-name">Tall FERN</span></div>
  </div>
  <div class="header-rule"></div>

  <p class="lead">Lorem ipsum dolor sit Lorem ipsum dolor sit &nbsp;Lorem ipsum dolor sit</p>
  <p class="intro">Lorem ipsum dolor sit Lorem ipsum dolor sit &nbsp;Lorem ipsum dolor sit Lorem ipsum dolor sit &nbsp;Lorem ipsum dolor sit Lorem ipsum dolor sit &nbsp;Lorem ipsum dolor sit Lorem ipsum dolor sit &nbsp;Lorem ipsum dolor sit Lorem ipsum dolor sit &nbsp;Lorem ipsum dolor sit Lorem ipsum dolor sit &nbsp;Lorem ipsum dolor sit Lorem ipsum dolor sit &nbsp;Lorem ipsum dolor sit Lorem ipsum dolor sit</p>

  <div class="timeline-line"></div>
  <div class="milestone" style="left:170px"><span class="milestone-fill is-green">1995</span></div>
  <div class="milestone" style="left:545px"><span class="milestone-fill is-lime">2005</span></div>
  <div class="milestone" style="left:923px"><span class="milestone-fill is-grey">2015</span></div>

  <div class="card is-green" style="left:59px">
    <div class="card-head">TITLE HERE</div>
    <p class="card-body">Lorem ipsum dolor sit Lorem ipsum dolor sit &nbsp;Lorem ipsum dolor sit Lorem ipsum dolor sit Lorem ipsum dolor sit Lorem ipsum dolor sit &nbsp;Lorem ipsum dolor sit Lorem ipsum dolor sit Lorem ipsum dolor sit Lorem ipsum dolor sit &nbsp;Lorem ipsum dolor sit</p>
  </div>
  <div class="card is-lime" style="left:435px">
    <div class="card-head">TITLE HERE</div>
    <p class="card-body">Lorem ipsum dolor sit Lorem ipsum dolor sit &nbsp;Lorem ipsum dolor sit Lorem ipsum dolor sit Lorem ipsum dolor sit Lorem ipsum dolor sit &nbsp;Lorem ipsum dolor sit Lorem ipsum dolor sit Lorem ipsum dolor sit Lorem ipsum dolor sit &nbsp;Lorem ipsum dolor sit</p>
  </div>
  <div class="card is-grey" style="left:816px; height:393px">
    <div class="card-head">TITLE HERE</div>
    <p class="card-body">Lorem ipsum dolor sit Lorem ipsum dolor sit &nbsp;Lorem ipsum dolor sit Lorem ipsum dolor sit Lorem ipsum dolor sit Lorem ipsum dolor sit &nbsp;Lorem ipsum dolor sit Lorem ipsum dolor sit Lorem ipsum dolor sit Lorem ipsum dolor sit &nbsp;Lorem ipsum dolor sit</p>
  </div>

  <div class="footer"></div>
</div>
</body>
</html>
```